property investment and development company needs a website

we need a website that looks professional and portrays trust for people looking to us to buy their house or investors looking to invest or joint venture with us.
We are based in the west midlands in the UK.
we deal mainly with residential housing, house to flats conversions, HMO's (houses in multiple ocupancy).
we require the website as a first point of contact with potential sellers, renters and investors so links or contact details that are easy to access or see would be good.
I have had logos designed by a brief harbor member and these can be used as guidance for the colour and style of the site.
Target Market(s)
joint venture investment partners, people looking to sell their house, people looking to rent from us.
Coding
Coded - Design and coding required
Number of Pages Required
3 page
Requirements
Must have
- project a professional appearance
- visable contact details

```html
<!DOCTYPE html>
<html lang="en">
<head>
<meta charset="utf-8">
<title>Thornfield Homes</title>
<link rel="stylesheet" href="https://fonts.googleapis.com/css2?family=Poppins:wght@400;500;600;700&family=Open+Sans:wght@400;600&display=swap">
<style>
:root{
  --navy:#1f2c4c;
  --blue:#2f72b8;
  --gold:#c9a46a;
  --dark:#141414;
  --ink:#222;
  --muted:#555;
  --line:#bfc6cf;
  --white:#fff;
}
*{box-sizing:border-box;margin:0;padding:0}
html,body{width:1200px;height:4390px;overflow:hidden;background:#fff}
body{font-family:"Open Sans",sans-serif;color:var(--ink);position:relative}
.abs{position:absolute}
h1,h2,h3,h4,.nav,.btn{font-family:"Poppins",sans-serif}

/* top bar */
.topbar{top:0;left:0;width:1200px;height:30px;background:var(--dark);color:#fff;font-size:12px}
.topbar .mail{left:95px;top:8px}
.topbar .addr{left:555px;top:8px}
.topbar .phone{left:965px;top:0;height:30px;padding:8px 18px;background:var(--gold);font-weight:600}
.ico{display:inline-block;vertical-align:-2px;margin-right:6px}

/* header */
.header{top:30px;left:0;width:1200px;height:110px;background:#fff}
.brand{display:flex;align-items:center;gap:12px;font-family:"Poppins",sans-serif;font-weight:600;font-size:22px;line-height:1.05;color:var(--navy);letter-spacing:1px}
.brand .mark{width:40px;height:40px;background:var(--gold)}
.header .brand{left:100px;top:32px}
.nav{right:88px;top:48px;display:flex;gap:48px;font-size:16px;font-weight:500;color:var(--ink)}
.nav .active{color:var(--blue)}

/* hero */
.hero{top:140px;left:0;width:1200px;height:578px;background:linear-gradient(180deg,#8ba7c9 0%,#6d7f95 45%,#3d4650 75%,#2b2f33 100%)}
.hero h1{position:absolute;top:195px;width:100%;text-align:center;color:#fff;font-size:100px;font-weight:700;letter-spacing:1px}
.hero p{position:absolute;top:318px;width:100%;text-align:center;color:#fff;font-family:"Poppins",sans-serif;font-size:38px;font-weight:600}
.arrow{position:absolute;top:270px;color:#fff;font-size:26px}

/* welcome */
.welcome-logo{left:130px;top:900px;width:270px;text-align:center;font-size:30px;justify-content:center;flex-direction:column}
.welcome-logo .mark{width:80px;height:80px}
.welcome{left:492px;top:832px;width:620px}
.welcome h2{font-size:38px;font-weight:500;color:var(--ink);line-height:1.1}
.welcome h3{font-size:38px;font-weight:500;color:var(--navy);line-height:1.1;margin-bottom:26px}
.welcome p{font-size:15px;line-height:1.75;color:var(--ink);margin-bottom:16px}
.btn{display:inline-block;font-size:15px;padding:9px 18px;color:#fff}
.btn-solid{background:var(--blue);border-radius:3px}
.btn-ghost{border:1px solid #fff;border-radius:3px}

/* split blocks */
.panel{width:600px;height:430px;color:#fff;padding:62px 80px 0 90px}
.panel h2{font-size:40px;font-weight:500;margin-bottom:26px}
.panel p{font-size:14.5px;line-height:1.75;text-align:justify;margin-bottom:20px}
.invest{top:1258px;left:0;background:var(--navy)}
.invest-photo{top:1258px;left:600px;width:600px;height:430px;background:linear-gradient(135deg,#cfe0a8 0%,#9cb87a 40%,#7a8f6c 70%,#c9c4ac 100%)}
.sell-photo{top:1688px;left:0;width:600px;height:428px;background:linear-gradient(135deg,#2c3b58 0%,#55698a 45%,#c4ccd6 75%,#e9eef3 100%)}
.sell{top:1688px;left:600px;height:428px;background:var(--blue);padding-left:80px}

/* team */
.team-title{top:2235px;width:1200px;text-align:center;font-size:40px;font-weight:500;color:var(--navy)}
.card{top:2415px;width:308px;height:265px;background:#fff;box-shadow:0 4px 14px rgba(0,0,0,.25);text-align:center;padding:95px 36px 0}
.card.featured{background:var(--blue);color:#fff}
.card h4{font-size:17px;font-weight:500}
.card .role{font-size:14px;color:var(--blue);margin-bottom:14px}
.card.featured .role{color:#fff}
.card p{font-size:13.5px;line-height:1.55;color:var(--muted)}
.card.featured p{color:#fff}
.avatar{position:absolute;top:-65px;left:50%;margin-left:-63px;width:126px;height:126px;border-radius:50%;border:4px solid #fff;box-shadow:0 0 0 2px var(--blue);background:linear-gradient(180deg,#c9d3de,#8d9aab)}
.slide-arrow{top:2535px;font-size:22px;color:#555}

/* blog */
.blog{top:2818px;left:0;width:1200px;height:636px;background:linear-gradient(180deg,#1c2a47 0%,#26375a 50%,#1a2540 100%)}
.blog h2{position:absolute;top:78px;width:100%;text-align:center;color:#fff;font-size:40px;font-weight:600}
.post{position:absolute;top:182px;left:152px;width:910px;height:366px;background:#fff;box-shadow:0 4px 16px rgba(0,0,0,.3)}
.post-photo{position:absolute;top:0;left:0;width:383px;height:366px;background:linear-gradient(135deg,#e8ecf0 0%,#9aa6b4 45%,#2e3744 100%)}
.post-body{position:absolute;left:428px;top:40px;width:445px}
.post-body h3{font-size:25px;font-weight:500;line-height:1.35;color:var(--ink);margin-bottom:18px}
.meta{font-size:13px;color:var(--blue);margin-bottom:18px;display:flex;gap:34px}
.post-body p{font-size:14px;line-height:1.7;color:var(--muted);margin-bottom:20px}
.btn-line{font-family:"Poppins",sans-serif;font-size:11px;font-weight:600;color:var(--navy);border:2px solid var(--blue);border-radius:20px;padding:5px 16px;display:inline-block}
.blog .arrow{top:300px;font-size:40px}

/* contact */
.contact{top:3525px;left:111px;width:400px}
.contact h2{font-size:36px;font-weight:500;color:var(--ink);margin-bottom:30px}
.field{border-bottom:1px solid #777;font-size:14px;color:var(--ink);padding:0 0 9px;margin-bottom:30px}
.map{top:3454px;left:615px;width:585px;height:533px;background:linear-gradient(135deg,#eef0ec 0%,#e4e7e2 60%,#dcdfda 100%)}

/* footer */
.footer{top:3987px;left:0;width:1200px;height:403px;background:#070707;color:#fff}
.footer .brand{position:absolute;left:95px;top:120px;color:#fff}
.socials{position:absolute;left:148px;top:205px;display:flex;gap:8px}
.socials span{width:18px;height:18px;background:#fff;border-radius:2px}
.fcol{position:absolute;top:80px;font-size:14px}
.fcol h4{font-size:17px;font-weight:500;margin-bottom:22px;letter-spacing:.5px}
.fcol li{list-style:none;line-height:2.15}
.fcol .lbl{font-weight:600;font-size:13px}
.fcol .item{margin-bottom:22px;line-height:1.5}
.copy{position:absolute;top:355px;width:100%;text-align:center;font-size:12px;color:#aaa}
.footer .rule{position:absolute;top:330px;left:0;width:100%;height:1px;background:#222}
</style>
</head>
<body>

<div class="abs topbar">
  <div class="abs mail"><svg class="ico" width="13" height="10" viewBox="0 0 13 10"><rect x=".5" y=".5" width="12" height="9" fill="none" stroke="#fff"/><path d="M.5 .5 6.5 5.5 12.5 .5" fill="none" stroke="#fff"/></svg>info@thornfieldhomes.co.uk</div>
  <div class="abs addr"><svg class="ico" width="10" height="13" viewBox="0 0 10 13"><path d="M5 0a5 5 0 0 0-5 5c0 4 5 8 5 8s5-4 5-8a5 5 0 0 0-5-5z" fill="#fff"/><circle cx="5" cy="5" r="2" fill="#141414"/></svg>12 Elmwood Lane, Ledbury, Herefordshire, HR8 2AB</div>
  <div class="abs phone"><svg class="ico" width="12" height="12" viewBox="0 0 12 12"><path d="M2 0l2 3-1 1.5a7 7 0 0 0 4.5 4.5L9 8l3 2-1.5 2C5 12 0 7 0 1.5z" fill="#fff"/></svg>01632 960418</div>
</div>

<header class="abs header">
  <div class="abs brand"><span class="mark"></span><span>THORNFIELD<br>HOMES</span></div>
  <nav class="abs nav"><span class="active">Home</span><span>About Us</span><span>Invest</span><span>Sell</span><span>Blog</span><span>Contact us</span></nav>
</header>

<section class="abs hero" role="img" aria-label="City skyline with a river bridge at dusk">
  <span class="arrow" style="left:78px">&#8249;</span>
  <h1>Thornfield Homes</h1>
  <p>Neque porro quisquam qui dolorem</p>
  <span class="arrow" style="right:78px">&#8250;</span>
</section>

<div class="abs brand welcome-logo"><span class="mark"></span><span>THORNFIELD<br>HOMES</span></div>
<section class="abs welcome">
  <h2>Welcome to</h2>
  <h3>Thornfield Homes &amp; Developments Ltd</h3>
  <p>Weare a property development and investment company that have our own portfolio and we are active investorswho pride ourselves in expanding our business organically.</p>
  <p>We ensure that whatever your property needs are we deliver bespoke services for our clients. For investors, sellers, landlords and tenants we bring knowledge to your next property decision, allowing you to make an informed decision.</p>
  <span class="btn btn-solid">Read More</span>
</section>

<section class="abs panel invest">
  <h2>Invest</h2>
  <p>We have our own portfolio and we are active investors, so our finger is on the pulse and we are currently looking for residential development investments &amp; commercial to residential conversions in cities or regional centres showing strong growth Our experience in the industry enables us to make extremely quick andwell-informed decisions. We follow the opportunities that are presented to us as well as sourcing</p>
  <span class="btn btn-ghost">Read More</span>
</section>
<div class="abs invest-photo" role="img" aria-label="Glass jar of coins with a small plant growing from it"></div>

<div class="abs sell-photo" role="img" aria-label="Business people reviewing charts on paper at a desk"></div>
<section class="abs panel sell">
  <h2>Sell</h2>
  <p>We undertake the necessary market research to evaluate an option that works for all parties involved. We will help guide you to make an informed decision on how to gain the maximum realistic value For those looking to achieve a fast and professional sale to experienced investors, we provide an approach that has been proven to work for many others.</p>
  <span class="btn btn-ghost">Read More</span>
</section>

<h2 class="abs team-title">Our Team</h2>
<span class="abs slide-arrow" style="left:70px">&#8249;</span>
<div class="abs card" style="left:111px"><div class="avatar" role="img" aria-label="Portrait of team member"></div><h4>Owen Hartley, A.A.</h4><div class="role">(Neque quisquam)</div><p>It is a long established fact that a reader will be distracted by the readable content of a page when looking at its layout.</p></div>
<div class="abs card featured" style="left:446px"><div class="avatar" role="img" aria-label="Portrait of team member"></div><h4>Nina Bramwell</h4><div class="role">(Neque quisquam)</div><p>It is a long established fact that a reader will be distracted by the readable content of a page when looking at its layout.</p></div>
<div class="abs card" style="left:784px"><div class="avatar" role="img" aria-label="Portrait of team member"></div><h4>Clara Whitcombe</h4><div class="role">(Neque quisquam)</div><p>It is a long established fact that a reader will be distracted by the readable content of a page when looking at its layout.</p></div>
<span class="abs slide-arrow" style="left:1118px">&#8250;</span>

<section class="abs blog" role="img" aria-label="Darkened city skyline background">
  <h2>Latest Blog</h2>
  <span class="arrow" style="left:88px">&#8249;</span>
  <article class="post">
    <div class="post-photo" role="img" aria-label="Businessman beside rising chart over model houses"></div>
    <div class="post-body">
      <h3>NEQUE PORRO QUISQUAM EST DOLOREM IPSUM QUIA DOLOR AMET,</h3>
      <div class="meta"><span>&#9635;&nbsp; March 26, 2019</span><span>&#9633;&nbsp; 2 comments</span></div>
      <p>Sed ut perspiciatis unde omnis iste natus error sit voluptatem accusantium doloremque laudantium, totam rem aperiam, eaque ipsa quae ab illo inventore veritatis et quasi architecto beatae vitae dicta sunt explicabo. Nemo enim ipsam voluptatem quia</p>
      <span class="btn-line">LEARN MORE</span>
    </div>
  </article>
  <span class="arrow" style="right:88px">&#8250;</span>
</section>

<section class="abs contact">
  <h2>Contact us</h2>
  <div class="field">Name *</div>
  <div class="field">E-mail *</div>
  <div class="field">Phone</div>
  <div class="field">Company</div>
  <div class="field">Message</div>
  <span class="btn btn-solid" style="border-radius:16px;padding:6px 28px">Submit</span>
</section>
<div class="abs map" role="img" aria-label="Street map showing the office location on Elmwood Lane"></div>

<footer class="abs footer">
  <div class="brand"><span class="mark"></span><span>THORNFIELD<br>HOMES</span></div>
  <div class="socials"><span></span><span></span><span></span><span></span></div>
  <div class="fcol" style="left:455px">
    <h4>CONTACT US</h4>
    <div class="item"><div class="lbl">&#9993; EMAIL ADDRESS</div>info@thornfieldhomes.co.uk</div>
    <div class="item"><div class="lbl">&#9742; PHONE NUMBER</div>07700 900214</div>
  </div>
  <div class="fcol" style="left:758px">
    <h4>ABOUT</h4>
    <ul><li>Home</li><li>About Us</li><li>Sell</li><li>Invest</li></ul>
  </div>
  <div class="fcol" style="left:980px">
    <h4>RESOURCES</h4>
    <ul><li>Blog</li><li>Team</li><li>Testimonials</li><li>Contact us</li></ul>
  </div>
  <div class="rule"></div>
  <div class="copy">© 2019 Company Name &nbsp;All right reserved</div>
</footer>

</body>
</html>
```